Heater product information sheets

I need the two product information sheets organized and laid out in a clean, easy to read attractive manner. These sheets are to advertise propane heaters for outdoor use and for wholesale to propane distributors, restaurants and homeowners that need to have propane heat as the winter ends and spring begins. They will be used for chilly evenings when people want to be outside eating, drinking and being social.
Updates

Low design quality

Target Market(s)

Restaurants, hospitality industry, special events, party rental companies, home owners with backyards

Font styles to use
Sans Serif

Requirements
Must have
• My logo in the document instead of k. Dahlby and company
Nice to have
• I would like to see Fire illustrated coming up the heaters and on the round glass, show it up the middle of the glass tube propane heater.

```html
<!DOCTYPE html>
<html lang="en">
<head>
<meta charset="utf-8">
<title>Propane Heater Product Sheets</title>
<link rel="stylesheet" href="https://fonts.googleapis.com/css2?family=Montserrat:wght@400;500;600;700;800;900&display=swap">
<style>
  :root {
    --teal: #0e5468;
    --orange: #f09a1c;
    --ink: #1c1c1c;
    --paper: #ffffff;
    --stage: #575757;
    --stripe: #e4e4e4;
  }
  * { box-sizing: border-box; margin: 0; padding: 0; }
  html, body { width: 1200px; height: 900px; overflow: hidden; }
  body {
    background: var(--stage);
    font-family: "Montserrat", Arial, sans-serif;
    color: var(--ink);
    position: relative;
  }
  .sheet {
    position: absolute;
    top: 101px;
    width: 540px;
    height: 697px;
    background: var(--paper);
    overflow: hidden;
  }
  .sheet--outdoor { left: 34px; }
  .sheet--glass { left: 625px; }

  .top-rule { position: absolute; left: 284px; top: 0; width: 212px; height: 4px; background: var(--teal); }
  .bottom-rule { position: absolute; left: 0; bottom: 0; width: 100%; height: 4px; background: var(--teal); }
  .stripe-band {
    position: absolute; left: 1px; top: 52px; width: 17px; height: 516px;
    background: repeating-linear-gradient(135deg, var(--stripe) 0 3px, transparent 3px 7px);
  }
  .product-photo {
    position: absolute; left: 43px; top: 55px; width: 198px; height: 513px;
    border-radius: 4px;
  }
  .sheet--outdoor .product-photo {
    background: linear-gradient(180deg, #d9dcdf 0%, #bfc3c6 18%, #2a2a2c 40%, #151516 100%);
  }
  .sheet--glass .product-photo {
    background: linear-gradient(180deg, #d6d8da 0%, #c6c9cc 15%, #e9ebec 45%, #1d1d1f 62%, #121213 100%);
  }

  .title {
    position: absolute; right: 44px; top: 40px;
    font-size: 44px; font-weight: 900; color: var(--teal);
    letter-spacing: 0.5px; white-space: nowrap; line-height: 1;
  }
  .subtitle {
    position: absolute; left: 284px; top: 80px; width: 212px; height: 30px;
    background: var(--orange); color: #fff;
    font-size: 19px; font-weight: 800; letter-spacing: 0.4px;
    display: flex; align-items: center; justify-content: center;
  }
  .section-head {
    position: absolute; left: 284px; width: 212px; height: 28px;
    border: 1.5px solid var(--orange);
    color: var(--teal); font-size: 16px; font-weight: 800; letter-spacing: 0.3px;
    padding-left: 15px; display: flex; align-items: center;
  }
  .section-head--specs { top: 132px; }
  .section-head--details { top: 253px; }

  .check-list { position: absolute; left: 284px; width: 212px; list-style: none; }
  .check-list--specs { top: 172px; }
  .check-list--details { top: 292px; }
  .check-list li {
    position: relative; padding-left: 15px;
    font-size: 9.2px; font-weight: 500; line-height: 12.3px;
    margin-bottom: 3.2px;
  }
  .check-list li::before, .usage-list li::before {
    content: ""; position: absolute; left: 0; top: 2px;
    width: 8px; height: 8px; border-radius: 50%;
    border: 1px solid var(--orange);
  }
  .check-list li::after, .usage-list li::after {
    content: ""; position: absolute; left: 2.6px; top: 3.8px;
    width: 2.2px; height: 3.6px;
    border-right: 1px solid var(--orange); border-bottom: 1px solid var(--orange);
    transform: rotate(45deg);
  }

  .note-bar {
    position: absolute; left: 284px; top: 493px; width: 212px; height: 26px;
    background: var(--orange); color: #fff;
    font-size: 16px; font-weight: 700; padding-left: 15px;
    display: flex; align-items: center;
  }
  .price-row { position: absolute; left: 284px; top: 527px; width: 212px; height: 20px; display: flex; }
  .price-label {
    width: 107px; background: var(--orange); color: #fff;
    font-size: 8.6px; font-weight: 700; padding-left: 15px;
    display: flex; align-items: center;
  }
  .price-value {
    flex: 1; background: var(--teal); color: #fff;
    font-size: 13px; font-weight: 500; padding-left: 14px;
    display: flex; align-items: center;
  }
  .price-value strong { font-weight: 800; margin-right: 3px; }
  .note-text {
    position: absolute; left: 299px; top: 553px; width: 200px;
    font-size: 9.2px; font-weight: 500; line-height: 12.3px;
  }
  .contact-bar {
    position: absolute; left: 284px; top: 590px; width: 212px; height: 20px;
    background: var(--orange); color: #fff;
    font-size: 10px; font-weight: 700; letter-spacing: 0.3px; padding-left: 15px;
    display: flex; align-items: center;
  }
  .company-name {
    position: absolute; left: 299px; top: 615px;
    font-size: 10.5px; font-weight: 700;
  }
  .contact-list { position: absolute; left: 287px; top: 633px; list-style: none; }
  .contact-list li {
    display: flex; align-items: center; gap: 5px;
    font-size: 9.2px; font-weight: 500; line-height: 12.6px;
    margin-bottom: 0.4px;
  }
  .contact-list svg { width: 7px; height: 7px; flex: none; }

  .usage-list { position: absolute; left: 64px; top: 604px; width: 162px; list-style: none; }
  .usage-list li {
    position: relative; padding-left: 14px;
    color: var(--orange); font-size: 9.2px; font-weight: 500; line-height: 10.4px;
    text-transform: uppercase;
    padding-bottom: 4px; margin-bottom: 5px;
    border-bottom: 1px solid var(--teal);
  }
  .usage-list li:last-child { border-bottom: none; }
  .usage-list li::before { border-color: var(--teal); top: 1px; }
  .usage-list li::after { border-color: var(--teal); top: 2.8px; }
</style>
</head>
<body>

<section class="sheet sheet--outdoor">
  <div class="top-rule"></div>
  <div class="stripe-band"></div>
  <div class="product-photo" role="img" aria-label="Photo of a black mushroom-style outdoor propane patio heater with a steel reflector top"></div>

  <h1 class="title">OUTDOOR</h1>
  <div class="subtitle">PROPANE HEATER</div>

  <h2 class="section-head section-head--specs">SPECIFICATIONS</h2>
  <ul class="check-list check-list--specs">
    <li>Powerful 48,000 BTU</li>
    <li>Black Powder Coated Finish</li>
    <li>Uses 20 lbs. Propane Tank</li>
    <li>CE, GS, AGA, CSA, with ETL certificate and ROHS approved.</li>
  </ul>

  <h2 class="section-head section-head--details">ADDITIONAL DETAILS</h2>
  <ul class="check-list check-list--details">
    <li>Commercial Quality</li>
    <li>For Outdoor Use Only</li>
    <li>Conforms to ANSI STD Z83.26-2014 Certified to CSA STD 2.37-2014 Gas-fired outdoor infrared patio heaters</li>
    <li>Safety Auto Shut Off Switch</li>
    <li>Thermostatic Control</li>
    <li>Base Diameter 17” - Anti-Tip Design</li>
    <li>Standard Wheels - Tilt &amp; Move</li>
    <li>Run time: 8-10 hours with standard 20 lbs. Propane tank</li>
    <li>88” Tall</li>
    <li>Heating Area: 200 sq. ft</li>
  </ul>

  <div class="note-bar">NOTE</div>
  <div class="price-row">
    <div class="price-label">Price: Starting at</div>
    <div class="price-value"><strong>$250</strong> each</div>
  </div>
  <p class="note-text">Assembly &amp; Delivery available upon request<br>Discounts for large quantity orders</p>

  <div class="contact-bar">TO RENT OR PURCHASE:</div>
  <p class="company-name">K. Dahlby &amp; Company</p>
  <ul class="contact-list">
    <li><svg viewBox="0 0 10 10"><path d="M2 1l2 2-1 1.3c.6 1.2 1.5 2.1 2.7 2.7L7 6l2 2-1.3 1.3C4.5 9 1 5.5.7 2.3z" fill="none" stroke="#f09a1c" stroke-width="0.9"/></svg>555-014-2290</li>
    <li><svg viewBox="0 0 10 10"><rect x="0.6" y="2" width="8.8" height="6" fill="none" stroke="#f09a1c" stroke-width="0.9"/><path d="M0.6 2l4.4 3.4L9.4 2" fill="none" stroke="#f09a1c" stroke-width="0.9"/></svg>Mara@KDeventrental.com</li>
    <li><svg viewBox="0 0 10 10"><circle cx="5" cy="3.6" r="2.4" fill="none" stroke="#f09a1c" stroke-width="0.9"/><path d="M5 6v3.6" stroke="#f09a1c" stroke-width="0.9"/></svg>42 Mill Creek Rd Fairhaven, NJ 07990</li>
  </ul>

  <ul class="usage-list">
    <li>Rentals for live events</li>
    <li>Rentals for restaurants &amp; catering halls</li>
    <li>Purchase for your home or business</li>
  </ul>
  <div class="bottom-rule"></div>
</section>

<section class="sheet sheet--glass">
  <div class="top-rule"></div>
  <div class="stripe-band"></div>
  <div class="product-photo" role="img" aria-label="Photo of a black glass tube propane patio heater with a wire guard around the tube and a steel reflector top"></div>

  <h1 class="title">GLASS TUBE</h1>
  <div class="subtitle">PROPANE HEATER</div>

  <h2 class="section-head section-head--specs">SPECIFICATIONS</h2>
  <ul class="check-list check-list--specs">
    <li>Powerful 48,000 BTU</li>
    <li>Black Powder Coated Finish</li>
    <li>Uses 20 lbs. Propane Tank</li>
    <li>CE, GS, AGA, CSA, with ETL certificate and ROHS approved.</li>
  </ul>

  <h2 class="section-head section-head--details">ADDITIONAL DETAILS</h2>
  <ul class="check-list check-list--details">
    <li>Commercial Quality</li>
    <li>For Outdoor Use Only</li>
    <li>Conforms to ANSI STD Z83.26-2014 Certified to CSA STD 2.37-2014 Gas-fired outdoor infrared patio heaters</li>
    <li>Safety Auto Shut Off Switch</li>
    <li>Thermostatic Control</li>
    <li>Base Diameter 17” - Anti-Tip Design</li>
    <li>Standard Wheels - Tilt &amp; Move</li>
    <li>Run time: 8-10 hours with standard 20 lbs. Propane tank</li>
    <li>96” Tall</li>
    <li>Heating Area: 200 sq. ft</li>
  </ul>

  <div class="note-bar">NOTE</div>
  <div class="price-row">
    <div class="price-label">Price: Starting at</div>
    <div class="price-value"><strong>$250</strong> each</div>
  </div>
  <p class="note-text">Assembly &amp; Delivery available upon request<br>Discounts for large quantity orders</p>

  <div class="contact-bar">TO RENT OR PURCHASE:</div>
  <p class="company-name">K. Dahlby &amp; Company</p>
  <ul class="contact-list">
    <li><svg viewBox="0 0 10 10"><path d="M2 1l2 2-1 1.3c.6 1.2 1.5 2.1 2.7 2.7L7 6l2 2-1.3 1.3C4.5 9 1 5.5.7 2.3z" fill="none" stroke="#f09a1c" stroke-width="0.9"/></svg>555-014-2290</li>
    <li><svg viewBox="0 0 10 10"><rect x="0.6" y="2" width="8.8" height="6" fill="none" stroke="#f09a1c" stroke-width="0.9"/><path d="M0.6 2l4.4 3.4L9.4 2" fill="none" stroke="#f09a1c" stroke-width="0.9"/></svg>Mara@KDeventrental.com</li>
    <li><svg viewBox="0 0 10 10"><circle cx="5" cy="3.6" r="2.4" fill="none" stroke="#f09a1c" stroke-width="0.9"/><path d="M5 6v3.6" stroke="#f09a1c" stroke-width="0.9"/></svg>42 Mill Creek Rd Fairhaven, NJ 07990</li>
  </ul>

  <ul class="usage-list">
    <li>Rentals for live events</li>
    <li>Rentals for restaurants &amp; catering halls</li>
    <li>Purchase for your home or business</li>
  </ul>
  <div class="bottom-rule"></div>
</section>

</body>
</html>
```